Driving School for Teens Mobile Site

Need a simple redesign of this website www.kelomotoring.com to be focused on mobile. We want to get more sign-ups via the calendar tool we have. The site needs to be friendly for teenagers and parents.

There are two main groups: IN-Car Driving and Classroom Courses.

Here are some samples of sites we like:
https://plumeva.co/
www.yobertin.com
www.lumacredito.com
http://brightlaneinstitute.net/

We can use bookorama for the scheduling or slotpicker.me - but we need the home page to be more clear and easier for people to sign up.

Right now it's too difficult to read things and we are looking for a complete redesign.

The problem right now is that we are not having a lot of the people who come to the site sign up or call us. People want all of the course information right on the main home page.

We want to prevent people from clicking on other pages - we want to show them all of our courses all on the home page and easily viewable on mobile.

Here is the link: www.kelomotoring.com

Calls to Action such as phone calls and registrations are the primary key to the design.

Target Market(s)

High School Students and Parents looking for a driving school

Industry/Entity Type

Driving School

Coding

Number of Pages Required

Font styles to use
Serif
Sans Serif

Colors
85abd2
85cae6
87cfc6
fbf289
fee18a
fbc994
f8ba93
f59195
ffffff

Requirements
Must have
• Must have calls to actions for people to register or list the phone number so they call to register. Really needs to be friendly and happy.
Nice to have
• Nice to have good font style
Should not have
• Too many colors. Please only use 3-4 colors consistently and follow the same rules throughout the page.

```html
<!DOCTYPE html>
<html lang="en">
<head>
<meta charset="utf-8">
<title>Kelo Motoring Institute</title>
<link href="https://fonts.googleapis.com/css2?family=Open+Sans:wght@400;600;700&display=swap" rel="stylesheet">
<style>
:root{
  --yellow:#fbf289;
  --peach:#f8ba93;
  --peach-light:#fbc994;
  --coral:#f59195;
  --coral-dark:#e9797e;
  --blue:#85abd2;
  --orange:#f6a124;
  --ink:#3a3a3a;
  --muted:#5f5f5f;
  --white:#ffffff;
}
*{margin:0;padding:0;box-sizing:border-box}
html,body{width:714px;height:1200px;overflow:hidden}
body{font-family:"Open Sans",Arial,sans-serif;color:var(--ink);background:var(--white);position:relative}
.abs{position:absolute}

.site-header{left:0;top:0;width:714px;height:69px;background:var(--yellow)}
.brand{left:45px;top:20px;display:flex;align-items:center;gap:8px}
.brand-dot{width:22px;height:22px;border-radius:50%;background:var(--orange)}
.brand-name{font-weight:700;font-size:17px;color:var(--orange);letter-spacing:.3px}
.signup{left:504px;top:10px;width:73px;height:23px;background:var(--peach);color:var(--white);font-size:7.5px;font-weight:700;display:flex;align-items:center;justify-content:center;gap:4px;letter-spacing:.4px}
.phone{left:592px;top:14px;color:var(--coral);font-size:10px;font-weight:600;display:flex;align-items:center;gap:6px}
.main-nav{top:44px;left:367px;display:flex;gap:22px;font-size:7.2px;font-weight:600;color:#222;letter-spacing:.2px}

.hero{left:0;top:69px;width:714px;height:315px;background:linear-gradient(100deg,#7d8aa0 0%,#a7a39e 35%,#8b8c90 60%,#5b6068 100%)}
.hero-title{left:0;top:117px;width:714px;text-align:center;color:var(--white);font-size:30px;font-weight:700;letter-spacing:.3px}
.btn{background:var(--peach);color:var(--white);font-weight:700;display:flex;align-items:center;justify-content:center}
.hero-btn{top:178px;height:29px;font-size:11px;letter-spacing:.3px}
.dots{top:288px;left:335px;display:flex;gap:5px}
.dots span{width:8px;height:8px;border-radius:50%;background:var(--white)}
.dots span.on{background:var(--orange)}

.tagline{left:0;top:384px;width:714px;height:64px;display:flex;align-items:center;justify-content:center;font-size:17px;font-weight:600;color:#666;letter-spacing:.3px}

.photo{background:linear-gradient(135deg,#6f7681,#c3c0bb 55%,#9aa0a8)}
.section-title{font-size:17px;font-weight:700;color:var(--blue);letter-spacing:.6px}
.price-list{list-style:none;font-size:9px;color:var(--muted)}
.price-list li{position:relative;height:26px}
.price-list .amount{position:absolute;top:0}
.register{width:133px;height:29px;font-size:11px;letter-spacing:.3px}

.contact{left:0;top:933px;width:714px;height:227px;background:var(--coral)}
.block-title{color:var(--white);font-size:17px;font-weight:700;letter-spacing:.6px}
.field{background:var(--white);font-size:8px;color:#555;padding:8px 9px}
.submit{left:45px;top:1098px;width:107px;height:28px;background:var(--yellow);font-size:8.5px;font-weight:700;color:#333;display:flex;align-items:center;justify-content:center;letter-spacing:.4px}
.hours{left:485px;top:989px;list-style:none;color:var(--white);font-size:7.5px;font-weight:700}
.hours li{display:flex;height:21px}
.hours .day{width:79px}
.site-footer{left:0;top:1160px;width:714px;height:40px;background:var(--coral-dark);color:var(--white);font-size:7.5px;font-weight:600;display:flex;align-items:center;padding-left:44px}
</style>
</head>
<body>

<header class="site-header abs">
  <div class="brand abs"><span class="brand-dot"></span><span class="brand-name">KELO MOTORING</span></div>
  <div class="signup abs">
    <svg width="7" height="7" viewBox="0 0 10 10"><rect x="1" y="2" width="8" height="7" fill="none" stroke="#fff" stroke-width="1.4"/><line x1="1" y1="4" x2="9" y2="4" stroke="#fff" stroke-width="1.4"/></svg>
    SIGN UP
  </div>
  <div class="phone abs">
    <svg width="8" height="8" viewBox="0 0 10 10"><path d="M2 1l2 2-1 1.5c.7 1.3 1.5 2.1 2.5 2.5L7 6l2 2-1.5 1.5C4 9 1 6 .5 2.5z" fill="#f59195"/></svg>
    555.014.2290
  </div>
  <nav class="main-nav abs"><span>IN-CAR DRIVING</span><span>CLASSROOM COURSES</span><span>DOCUMENTS</span><span>ABOUT US</span></nav>
</header>

<section class="hero abs" role="img" aria-label="Photo of a teen student driver with an instructor in a car">
</section>
<h1 class="hero-title abs">We are a driving school for Teens</h1>
<a class="btn hero-btn abs" style="left:200px;width:149px;top:247px">In Car Driving Lessons</a>
<a class="btn hero-btn abs" style="left:365px;width:149px;top:247px">Classroom Courses</a>
<div class="dots abs" style="top:357px"><span class="on"></span><span></span><span></span><span></span></div>

<p class="tagline abs">Free Pick-up &amp; Drop Off From School, Home, Or Work!</p>

<div class="photo abs" style="left:0;top:448px;width:357px;height:242px" role="img" aria-label="Photo of a smiling young driver at the wheel with an instructor"></div>
<h2 class="section-title abs" style="left:392px;top:475px">DRIVING COURSES</h2>
<ul class="price-list abs" style="left:393px;top:507px;width:240px">
  <li>Behind the Wheel for Teens<span class="amount" style="left:198px">$279.00</span></li>
  <li>Behind the Wheel for Adults<span class="amount" style="left:198px">$350.00</span></li>
  <li>Use of KMI Vehicle for Driving Test<span class="amount" style="left:198px">$100.00</span></li>
  <li>90 Minute Parent/Teen Course<span class="amount" style="left:198px">$ 50.00</span></li>
</ul>
<a class="btn register abs" style="left:393px;top:620px">Register Now</a>

<h2 class="section-title abs" style="left:43px;top:739px">CLASSROOM COURSES</h2>
<ul class="price-list abs" style="left:44px;top:772px;width:240px">
  <li>Learner's Permit 8 Hour course<span class="amount" style="left:198px">$250.00</span></li>
  <li>Learner's Permit Re-Examination<span class="amount" style="left:198px">$250.00</span></li>
  <li>Drivers Education for teens<span class="amount" style="left:198px">$279.00</span></li>
</ul>
<a class="btn register abs" style="left:44px;top:865px">Register Now</a>
<div class="photo abs" style="left:357px;top:690px;width:357px;height:243px;background:linear-gradient(135deg,#c9cfc8,#d9b39c 50%,#5a7c8a)" role="img" aria-label="Photo of happy students holding a speed limit sign and a new licence"></div>

<section class="contact abs">
  <h2 class="block-title abs" style="left:44px;top:27px">CONTACT US</h2>
  <div class="field abs" style="left:45px;top:60px;width:196px;height:29px">Name</div>
  <div class="field abs" style="left:45px;top:93px;width:196px;height:29px">Email Address</div>
  <div class="field abs" style="left:45px;top:127px;width:196px;height:29px">Phone No.</div>
  <div class="field abs" style="left:258px;top:60px;width:198px;height:96px">Message</div>
  <h2 class="block-title abs" style="left:485px;top:27px">HOURS</h2>
</section>
<div class="submit abs">SUBMIT</div>
<ul class="hours abs">
  <li><span class="day">MONDAY</span>9:00AM - 7:00PM</li>
  <li><span class="day">TUESDAY</span>9:00AM - 7:00PM</li>
  <li><span class="day">WEDNESDAY</span>9:00AM - 7:00PM</li>
  <li><span class="day">THURSDAY</span>9:00AM - 7:00PM</li>
  <li><span class="day">FRIDAY</span>9:00AM - 7:00PM</li>
  <li><span class="day">SATURDAY</span>9:00AM - 2:00PM</li>
  <li><span class="day">SUNDAY</span>9:00AM - 12:00PM</li>
</ul>

<footer class="site-footer abs">Copyright © 2016. Kelo Motoring Institute. All Right Reserved</footer>

</body>
</html>
```